fun, modern poster design for office environment

We are a Corporate Health consultants and are looking for posters encouraging staff to be healthy.
Wanted: A5 poster design encouraging office workers to take the stairs rather than lift.
Posters will be displayed around the office and near the stairs
Poster will have health benefits included and should have a fun modern feel.
More poster designs to follow.

Target Market(s)

Men and some aged between 20 and 55.

Industry/Entity Type

Environment

Font styles to use
Sans Serif

Colors
0792cd
00a990
9ccb3b
86cfc6
fbf289
fcca95
ffffff
3277b5

Requirements
Must have
• A5 size
• Wording 'take the stairs' and a health benefit of taking be stairs.
• My company logo and name Harbinger Collective
• Web address www.harbingercollective.com.au
Nice to have
• Images and words
Should not have
• Stick people or people images.

```html
<!DOCTYPE html>
<html lang="en">
<head>
<meta charset="utf-8">
<title>Take the Stairs – Harbinger Collective</title>
<link rel="stylesheet" href="https://fonts.googleapis.com/css2?family=Asap+Condensed:wght@600;700&family=Catamaran:wght@800&display=swap">
<style>
  :root {
    --page: #f4f2f3;
    --poster-blue: #2b78b6;
    --step-blue: #7dd0f5;
    --step-yellow: #f8f28c;
    --step-peach: #fbcb98;
    --white: #ffffff;
    --navy: #1f3563;
  }
  * { margin: 0; padding: 0; box-sizing: border-box; }
  html, body {
    width: 1200px; height: 1200px; overflow: hidden;
    background: var(--page);
  }
  .poster {
    position: absolute; left: 307px; top: 194px;
    width: 586px; height: 812px;
    background: var(--white);
    overflow: hidden;
  }
  .sky, .stairs-art {
    position: absolute; inset: 0; width: 100%; height: 100%;
  }
  .headline {
    position: absolute; left: 0; right: 0; top: 110px;
    text-align: center;
    font-family: "Catamaran", sans-serif; font-weight: 800;
    font-size: 52px; letter-spacing: 0.5px; line-height: 1;
    color: var(--white);
  }
  .benefit {
    position: absolute;
    font-family: "Asap Condensed", sans-serif; font-weight: 700;
    font-size: 24px; line-height: 26px; letter-spacing: 0.6px;
    color: var(--white); white-space: nowrap;
  }
  .benefit--wrap { text-align: center; }
  .benefit::before { content: "\2022\00a0"; }
  .benefit--1 { left: 111px; top: 257px; }
  .benefit--2 { left: 153px; top: 305px; letter-spacing: 1.6px; }
  .benefit--3 { left: 221px; top: 364px; }
  .benefit--4 { left: 293px; top: 420px; }
  .benefit--5 { left: 377px; top: 488px; }
  .brand-mark {
    position: absolute; left: 103px; top: 606px;
    width: 108px; height: 108px; border-radius: 50%;
    border: 4px solid var(--navy);
  }
  .brand-name {
    position: absolute; left: 49px; top: 722px;
    font-family: "Asap Condensed", sans-serif; font-weight: 600;
    font-size: 26px; line-height: 1; color: var(--navy);
  }
  .brand-web {
    position: absolute; left: 49px; top: 757px;
    font-family: "Asap Condensed", sans-serif; font-weight: 600;
    font-size: 15px; line-height: 1; color: var(--navy);
  }
</style>
</head>
<body>
  <main class="poster">
    <svg class="sky" viewBox="0 0 488 677" preserveAspectRatio="none" aria-hidden="true">
      <polygon fill="var(--poster-blue)" points="0,0 488,0 488,560 0,230"/>
    </svg>

    <svg class="stairs-art" viewBox="0 0 488 677" preserveAspectRatio="none"
         role="img" aria-label="Illustration of a colourful staircase arrow climbing from lower right to upper left">
      <defs>
        <linearGradient id="stairs-band" gradientUnits="userSpaceOnUse" x1="200" y1="365" x2="150" y2="440">
          <stop offset="0" stop-color="var(--step-blue)"/>
          <stop offset="0.5" stop-color="var(--step-yellow)"/>
          <stop offset="1" stop-color="var(--step-peach)"/>
        </linearGradient>
      </defs>
      <polygon fill="url(#stairs-band)" points="0,230 488,560 488,660 0,300"/>
    </svg>

    <h1 class="headline">TAKE THE STAIRS</h1>

    <p class="benefit benefit--1">IS A HEALTHIER OPTION THAN THE LIFT</p>
    <p class="benefit benefit--2">BUILDS MUSCLES</p>
    <p class="benefit benefit--3">BURNS CALORIES</p>
    <p class="benefit benefit--4 benefit--wrap">CUTS DOWN ON CARBON<br>USE</p>
    <p class="benefit benefit--5 benefit--wrap">GREAT FOR YOUR<br>HEART</p>

    <div class="brand-mark" aria-hidden="true"></div>
    <p class="brand-name">Harbinger Collective</p>
    <p class="brand-web">www.harbingercollective.com.au</p>
  </main>
</body>
</html>
```